Kestrel Plumbing business card full re design & logo design

Kestrel Plumbing is a Sydney based mechanical plumbing contractor company.
We would like a full redesign with new logo etc which we can take to a future website, uniforms, vehicle sign writing etc.
Blue is my preferred choice of colour but i would be open to see a couple of alternatives thrown in the mix to see how they compare. I am open to see on white cards, black cards etc. Open to many new ideas.
Please see attached original business cards which have been used for the last 5 years.

Target Market(s)

Mechanical services industry.

Industry/Entity Type

Plumbing

Contact Information for Business Card

Dale Fenmore
Director

Mob: 0427 596 418
Email: dale@kestrelplumbing-demo.net.au
PO BOX 782
Harwood Vale NSW 2160
Lic: 518604k

Logo Text

Kestrel Plumbing

Font styles to use
Sans Serif

Colors
0655a3
3276b5
0792cd
33a6d7
85cae6
000000
333333
474747

Requirements
Must have
• Things that make it very professional and very well presented.
Nice to have
• Same description or very similar to attached uploaded file
Should not have
• Anything that makes it look unprofessional or cartoony.

```html
<!DOCTYPE html>
<html lang="en">
<head>
<meta charset="utf-8">
<title>Kestrel Plumbing – Business Card</title>
<link href="https://fonts.googleapis.com/css2?family=Teko:wght@500;600&family=Russo+One&family=Saira+Condensed:wght@300&family=Orbitron:wght@500&display=swap" rel="stylesheet">
<style>
  :root {
    --page: #e0dcdd;
    --card: #5a5a5a;
    --card-dark: #4a4a4a;
    --ribbon: #1592d0;
    --ribbon-fold: #0a5fa0;
    --steel: #6b92ad;
    --white: #ffffff;
    --ink: #111111;
  }
  * { margin: 0; padding: 0; box-sizing: border-box; }
  html, body { width: 1200px; height: 1200px; overflow: hidden; background: var(--page); }
  .canvas { position: relative; width: 1200px; height: 1200px; }

  .card {
    position: absolute;
    background: var(--card);
    overflow: hidden;
    box-shadow: 10px 10px 14px rgba(0,0,0,0.55);
  }
  .card--front { left: 154px; top: 34px; width: 900px; height: 540px; }
  .card--back  { left: 146px; top: 620px; width: 917px; height: 550px; }

  .card__bands { position: absolute; inset: 0; }

  .name-ribbon { position: absolute; left: 0; top: 0; width: 900px; height: 540px; }
  .name-block { position: absolute; left: 35px; top: 198px; color: var(--white); font-family: "Teko", sans-serif; }
  .name-block__name { font-weight: 600; font-size: 52px; line-height: 1; letter-spacing: 1px; }
  .name-block__role { font-weight: 500; font-size: 24px; line-height: 1; margin-top: -4px; letter-spacing: 1px; }

  .brand { position: absolute; left: 378px; top: 70px; display: flex; align-items: center; gap: 14px; }
  .brand__mark { width: 70px; height: 70px; background: var(--ribbon); }
  .brand__name { font-family: "Teko", sans-serif; font-weight: 600; font-size: 44px; color: var(--white); line-height: 1; padding-top: 18px; letter-spacing: 0.5px; }

  .contact { position: absolute; display: flex; align-items: center; gap: 10px;
    font-family: "Teko", sans-serif; font-weight: 500; color: var(--white); font-size: 24px; line-height: 1; letter-spacing: 0.5px; }
  .contact__icon { width: 46px; height: 46px; border-radius: 50%; background: var(--white); flex: none; display: flex; align-items: center; justify-content: center; }
  .contact__icon svg { width: 28px; height: 28px; }
  .contact--phone { left: 523px; top: 152px; }
  .contact--email { left: 523px; top: 227px; font-size: 21px; }
  .contact--licence { left: 523px; top: 291px; }
  .contact--address { left: 66px; top: 427px; gap: 16px; }
  .contact--address .contact__icon { width: 56px; height: 56px; }
  .contact--address .contact__icon svg { width: 32px; height: 32px; }
  .contact__lines span { display: block; padding-top: 4px; }

  .services-title { position: absolute; left: 86px; top: 62px; white-space: nowrap;
    font-family: "Russo One", sans-serif; font-size: 40px; color: var(--white); letter-spacing: 0; line-height: 1; }
  .services-sub { position: absolute; right: 80px; top: 118px; font-family: "Saira Condensed", sans-serif; font-weight: 300;
    font-size: 56px; color: var(--white); line-height: 1; }
  .services-list { position: absolute; left: 396px; top: 198px; list-style: none;
    font-family: "Saira Condensed", sans-serif; font-weight: 300; font-size: 44px; color: var(--white); line-height: 1; }
  .services-list li { display: flex; align-items: center; gap: 6px; height: 53px; }
  .services-list li:nth-child(n+4) { height: 50px; }
  .services-list svg { width: 20px; height: 20px; fill: var(--white); }

  .back-brand { position: absolute; left: 62px; top: 236px; width: 290px;
    font-family: "Russo One", sans-serif; font-size: 54px; line-height: 1.1; color: var(--steel); }
  .back-tagline { position: absolute; left: 46px; top: 459px; font-family: "Orbitron", sans-serif; font-weight: 500;
    font-size: 14px; color: var(--white); letter-spacing: 1px; word-spacing: 6px; white-space: nowrap; }
</style>
</head>
<body>
<main class="canvas">

  <section class="card card--front">
    <svg class="card__bands" viewBox="0 0 900 540" aria-hidden="true">
      <defs>
        <linearGradient id="bandShade" x1="0" y1="0" x2="1" y2="0">
          <stop offset="0" stop-color="#3e3e3e"/>
          <stop offset="1" stop-color="#5a5a5a"/>
        </linearGradient>
      </defs>
      <polygon points="224,0 302,0 550,540 474,540" fill="var(--card-dark)"/>
      <polygon points="302,0 330,0 590,540 550,540" fill="url(#bandShade)" opacity="0.8"/>
      <polygon points="302,0 900,0 900,540 590,540" fill="var(--card)"/>
      <polygon points="224,0 240,0 486,540 474,540" fill="#666666"/>
    </svg>

    <svg class="name-ribbon" viewBox="0 0 900 540" aria-hidden="true">
      <polygon points="357,290 394,290 380,340" fill="var(--ribbon-fold)"/>
      <polygon points="0,172 339,172 394,290 0,290" fill="var(--ribbon)"/>
    </svg>
    <div class="name-block">
      <div class="name-block__name">DALE FENMORE</div>
      <div class="name-block__role">DIRECTOR</div>
    </div>

    <div class="brand">
      <div class="brand__mark"></div>
      <div class="brand__name">KESTREL PLUMBING</div>
    </div>

    <div class="contact contact--phone">
      <span class="contact__icon"><svg viewBox="0 0 24 24"><circle cx="12" cy="12" r="10.5" fill="none" stroke="var(--ink)" stroke-width="1.6"/><path d="M8 7c1-1 2-.5 2.5.5l.6 1.4c.2.6 0 1-.4 1.4l-.7.6c.6 1.4 1.7 2.6 3.1 3.2l.6-.7c.4-.4.8-.6 1.4-.4l1.4.6c1 .5 1.4 1.5.5 2.5-1.4 1.4-3.7 1-6-1.3S6.6 8.4 8 7z" fill="var(--ink)"/></svg></span>
      <span>0427 596 418</span>
    </div>
    <div class="contact contact--email">
      <span class="contact__icon"><svg viewBox="0 0 24 24"><rect x="3" y="6" width="18" height="12" fill="var(--ink)"/><path d="M3 6l9 7 9-7M3 18l7-6M21 18l-7-6" fill="none" stroke="var(--white)" stroke-width="1.2"/></svg></span>
      <span>DALE@KESTRELPLUMBING-DEMO.NET.AU</span>
    </div>
    <div class="contact contact--licence">
      <span class="contact__icon"><svg viewBox="0 0 24 24"><rect x="5" y="5" width="12" height="16" fill="none" stroke="var(--ink)" stroke-width="1.4"/><rect x="8" y="3" width="6" height="3" fill="var(--ink)"/><path d="M8 10h6M8 13h6M8 16h6" stroke="var(--ink)" stroke-width="1.2"/><path d="M19 7v12" stroke="var(--ink)" stroke-width="1.6"/></svg></span>
      <span>518604K</span>
    </div>
    <div class="contact contact--address">
      <span class="contact__icon"><svg viewBox="0 0 24 24"><path d="M12 2a6 6 0 0 0-6 6c0 4.5 6 11 6 11s6-6.5 6-11a6 6 0 0 0-6-6z" fill="var(--ink)"/><circle cx="12" cy="8" r="2.4" fill="var(--white)"/><ellipse cx="12" cy="21" rx="5" ry="1.4" fill="none" stroke="var(--ink)" stroke-width="1.2"/></svg></span>
      <span class="contact__lines"><span>PO BOX 782</span><span>HARWOOD VALE NSW 2160</span></span>
    </div>
  </section>

  <section class="card card--back">
    <h1 class="services-title">MECHANICAL PLUMBING SERVICES</h1>
    <p class="services-sub">Specialising in:</p>

    <div class="back-brand">KESTREL PLUMBING</div>
    <p class="back-tagline">KESTREL &nbsp; DELIVER THE RESULT</p>

    <ul class="services-list">
      <li><svg viewBox="0 0 24 24"><path d="M12 2l2.9 6.9 7.1.6-5.4 4.7 1.7 7.3L12 17.6 5.7 21.5l1.7-7.3L2 9.5l7.1-.6z"/></svg>Make Good</li>
      <li><svg viewBox="0 0 24 24"><path d="M12 2l2.9 6.9 7.1.6-5.4 4.7 1.7 7.3L12 17.6 5.7 21.5l1.7-7.3L2 9.5l7.1-.6z"/></svg>Refurbishment</li>
      <li><svg viewBox="0 0 24 24"><path d="M12 2l2.9 6.9 7.1.6-5.4 4.7 1.7 7.3L12 17.6 5.7 21.5l1.7-7.3L2 9.5l7.1-.6z"/></svg>Tenancy Fit Out</li>
      <li><svg viewBox="0 0 24 24"><path d="M12 2l2.9 6.9 7.1.6-5.4 4.7 1.7 7.3L12 17.6 5.7 21.5l1.7-7.3L2 9.5l7.1-.6z"/></svg>Plant Room Works</li>
      <li><svg viewBox="0 0 24 24"><path d="M12 2l2.9 6.9 7.1.6-5.4 4.7 1.7 7.3L12 17.6 5.7 21.5l1.7-7.3L2 9.5l7.1-.6z"/></svg>Shut Downs</li>
      <li><svg viewBox="0 0 24 24"><path d="M12 2l2.9 6.9 7.1.6-5.4 4.7 1.7 7.3L12 17.6 5.7 21.5l1.7-7.3L2 9.5l7.1-.6z"/></svg>Change Overs</li>
    </ul>
  </section>

</main>
</body>
</html>
```